Delvane Advisory Partners
Simple
Dr. Paul Merideth
347 Brookfield Lane
Los Altos, CA 94024
mtorvell@delvaneadvisorypartners.example
www.delvaneadvisorypartners.example
I wish to create a classy, simple, elegant single-sided business card for my consulting company.
I only wish for my number, e-mail, and website information to be on the card, NOT my address. Also, no need to put "cell" or "e-mail" or "web" on the card, just the information.

```html
<!DOCTYPE html>
<html lang="en">
<head>
<meta charset="utf-8">
<title>Delvane Advisory Partners — Stationery Concepts</title>
<link href="https://fonts.googleapis.com/css2?family=Cinzel:wght@400;500&family=Lato:wght@300;400&display=swap" rel="stylesheet">
<style>
  :root {
    --backdrop: #5a3a22;
    --paper: #ffffff;
    --paper-shade: #eeeeee;
    --ink: #2b2b2b;
    --ink-soft: #777777;
    --card-dark: #151515;
    --light-text: #f2ece4;
    --caption: #d9c8b4;
  }
  * { box-sizing: border-box; margin: 0; padding: 0; }
  html, body { width: 1200px; height: 439px; overflow: hidden; }
  body {
    position: relative;
    background: var(--backdrop);
    font-family: "Lato", sans-serif;
    color: var(--ink);
  }
  .abs { position: absolute; }

  .brand-name {
    font-family: "Cinzel", serif;
    font-weight: 400;
    text-align: center;
    letter-spacing: 0.06em;
    line-height: 1.1;
  }

  /* Intro block */
  .intro { left: 30px; top: 76px; width: 165px; color: var(--light-text); text-align: center; }
  .intro .brand-name { font-size: 22px; }
  .intro .brand-name small { display: block; font-size: 9px; letter-spacing: 0.22em; margin-top: 3px; }
  .intro .subtitle { font-size: 9px; letter-spacing: 0.1em; margin-top: 6px; font-family: "Cinzel", serif; }

  /* Business cards */
  .card { left: 43px; width: 139px; height: 84px; border-radius: 4px; padding: 10px 8px; text-align: center; }
  .card-front { top: 163px; background: var(--paper); }
  .card-back { top: 278px; background: var(--card-dark); color: var(--light-text); }
  .card .brand-name { font-size: 11px; }
  .card .brand-name small { display: block; font-size: 5px; letter-spacing: 0.2em; margin-top: 2px; }
  .card .holder { font-size: 5.5px; margin-top: 9px; }
  .card .details { font-size: 4.2px; line-height: 1.5; margin-top: 5px; color: var(--ink-soft); }
  .card-back .details { color: #bbbbbb; }

  /* Letterheads */
  .letterhead { top: 24px; width: 274px; height: 384px; background: var(--paper); }
  .letterhead-one { left: 226px; }
  .letterhead-two { left: 533px; }
  .letterhead .masthead { position: absolute; top: 14px; left: 20px; }
  .letterhead-two .masthead { left: 0; right: 0; }
  .letterhead .brand-name { font-size: 11px; }
  .letterhead .brand-name small { display: block; font-size: 4.5px; letter-spacing: 0.22em; margin-top: 2px; }
  .letterhead .contact { position: absolute; top: 14px; left: 150px; font-size: 3.6px; line-height: 1.6; color: var(--ink-soft); border-left: 0.5px solid #bbb; padding-left: 4px; }
  .letterhead .footer { position: absolute; bottom: 8px; left: 0; right: 0; text-align: center; font-size: 3.6px; color: var(--ink-soft); }

  /* Envelopes */
  .envelope { left: 830px; width: 327px; }
  .envelope svg { display: block; }
  .envelope-dark { top: 24px; height: 96px; }
  .envelope-open { top: 113px; height: 127px; }
  .envelope-long { top: 252px; height: 137px; background: var(--paper); }
  .envelope-long .masthead { position: absolute; top: 12px; left: 14px; }
  .envelope-long .brand-name { font-size: 11px; text-align: left; }
  .envelope-long .brand-name small { display: block; font-size: 4.5px; letter-spacing: 0.22em; margin-top: 2px; }

  .caption { top: 412px; font-size: 5px; color: var(--caption); letter-spacing: 0.05em; }
</style>
</head>
<body>

  <header class="abs intro">
    <div class="brand-name">DELVANE<small>ADVISORY PARTNERS</small></div>
    <div class="subtitle">Stationery Concepts</div>
  </header>

  <section class="abs card card-front">
    <div class="brand-name">DELVANE<small>ADVISORY PARTNERS</small></div>
    <div class="holder">Dr. Paul Merideth</div>
    <div class="details">650.555.0148<br>mtorvell@delvaneadvisorypartners.example<br>www.delvaneadvisorypartners.example</div>
  </section>
  <div class="abs caption" style="left:80px;top:252px;">Front of card</div>

  <section class="abs card card-back">
    <div class="brand-name">DELVANE<small>ADVISORY PARTNERS</small></div>
    <div class="holder">Dr. Paul Merideth</div>
    <div class="details">650.555.0148<br>mtorvell@delvaneadvisorypartners.example<br>www.delvaneadvisorypartners.example</div>
  </section>
  <div class="abs caption" style="left:82px;top:366px;">Back of card</div>

  <section class="abs letterhead letterhead-one">
    <div class="masthead"><div class="brand-name">DELVANE<small>ADVISORY PARTNERS</small></div></div>
    <div class="contact">650.555.0148<br>mtorvell@delvaneadvisorypartners.example<br>www.delvaneadvisorypartners.example</div>
  </section>
  <div class="abs caption" style="left:340px;">Letterhead page one</div>

  <section class="abs letterhead letterhead-two">
    <div class="masthead"><div class="brand-name">DELVANE<small>ADVISORY PARTNERS</small></div></div>
    <div class="footer">347 Brookfield Lane · Los Altos, CA 94024 · 650.555.0148 · mtorvell@delvaneadvisorypartners.example</div>
  </section>
  <div class="abs caption" style="left:647px;">Letterhead page two</div>

  <section class="abs envelope envelope-dark">
    <svg width="327" height="96" viewBox="0 0 327 96">
      <rect width="327" height="96" fill="var(--paper)"/>
      <polygon points="0,0 327,0 163.5,70" fill="var(--card-dark)"/>
    </svg>
  </section>

  <section class="abs envelope envelope-open">
    <svg width="327" height="127" viewBox="0 0 327 127">
      <polygon points="0,30 163.5,0 327,30" fill="var(--paper-shade)"/>
      <rect y="30" width="327" height="97" fill="var(--paper)"/>
      <polyline points="0,127 150,70 177,70 327,127" fill="none" stroke="#cfcfcf" stroke-width="1"/>
      <polyline points="0,30 163.5,85 327,30" fill="none" stroke="#dddddd" stroke-width="1"/>
    </svg>
  </section>

  <section class="abs envelope envelope-long">
    <div class="masthead"><div class="brand-name">DELVANE<small>ADVISORY PARTNERS</small></div></div>
  </section>
  <div class="abs caption" style="left:1120px;">Envelope set</div>

</body>
</html>
```